Business / Stationery Design Project

Hi,

I need business cards and all other stationary designed for my new finance broking business.

Stationary required:

Business card
Letter head
with compliments
envelopes

There is gold in the logo design so some gold would be good and open to other creative ideas / colours.

Regards
Tomas
Updates

Project Deadline Extended
Reason: Still working through designs.

Target Market(s)

Small to medium business customers. Also to appeal to referrers who include accounting firms and other associated professionals (valuers etc)

Industry/Entity Type

Finance

Requirements
Must have
• Professional, classy look.

```html
<!DOCTYPE html>
<html lang="en">
<head>
<meta charset="utf-8">
<title>Halden Finance – Business Card</title>
<link href="https://fonts.googleapis.com/css2?family=Source+Sans+3:wght@400;600;700&display=swap" rel="stylesheet">
<style>
  :root {
    --gold: #c9a865;
    --gold-deep: #b8955a;
    --ink: #1e1c1c;
    --paper: #ffffff;
    --muted: #4a4a4a;
    --stage: #ecebe8;
  }
  * { margin: 0; padding: 0; box-sizing: border-box; }
  html, body { width: 1200px; height: 748px; overflow: hidden; }
  body {
    background: var(--stage);
    font-family: "Source Sans 3", "Myriad Pro", sans-serif;
    position: relative;
  }
  .card {
    position: absolute;
    top: 219px;
    width: 540px;
    height: 310px;
    border-radius: 26px;
    overflow: hidden;
    box-shadow: 0 6px 18px rgba(0,0,0,0.18);
  }
  .card--front { left: 40px; background: var(--paper); }
  .card--back { left: 620px; background: var(--gold); }

  .front-swoosh { position: absolute; inset: 0; }

  .brand {
    position: absolute;
    left: 34px;
    top: 96px;
    color: var(--ink);
    font-weight: 600;
    line-height: 1;
  }
  .brand__name { font-size: 50px; letter-spacing: 1px; display: block; }
  .brand__sub { font-size: 18px; letter-spacing: 14px; display: block; margin-top: 6px; padding-left: 40px; }

  .holder {
    position: absolute;
    right: 40px;
    top: 36px;
    text-align: right;
  }
  .holder__name { color: var(--gold); font-weight: 700; font-size: 20px; }
  .holder__title { color: var(--muted); font-size: 13px; }

  .contact {
    position: absolute;
    right: 40px;
    top: 104px;
    list-style: none;
    text-align: right;
    color: var(--muted);
    font-size: 13.5px;
    line-height: 18px;
  }
  .contact li { display: flex; justify-content: flex-end; align-items: center; gap: 5px; }
  .contact svg { width: 9px; height: 9px; fill: var(--muted); }

  .address {
    position: absolute;
    left: 34px;
    bottom: 30px;
    color: var(--paper);
    font-size: 15px;
    line-height: 18px;
  }

  .back-brand {
    position: absolute;
    left: 0; right: 0;
    top: 112px;
    text-align: center;
    color: var(--paper);
    font-weight: 600;
    font-size: 40px;
    letter-spacing: 2px;
  }
  .back-web {
    position: absolute;
    left: 0; right: 0;
    bottom: 40px;
    text-align: center;
    color: var(--paper);
    font-size: 19px;
    letter-spacing: 3px;
  }
</style>
</head>
<body>
  <section class="card card--front">
    <svg class="front-swoosh" viewBox="0 0 540 310" preserveAspectRatio="none" aria-hidden="true">
      <path d="M0 234 C160 228 380 226 540 212 L540 310 L0 310 Z" fill="var(--gold)"/>
      <path d="M70 230 C250 224 420 214 540 194 L540 204 C420 222 250 228 70 230 Z" fill="var(--ink)"/>
      <path d="M200 226 C340 220 450 206 540 184 L540 190 C450 212 340 222 200 226 Z" fill="var(--gold)"/>
    </svg>
    <div class="brand">
      <span class="brand__name">HALDEN</span>
      <span class="brand__sub">FINANCE</span>
    </div>
    <div class="holder">
      <p class="holder__name">Greg Tomas</p>
      <p class="holder__title">Title</p>
    </div>
    <ul class="contact">
      <li><svg viewBox="0 0 10 10"><path d="M2 0 L4 2 L3 3.5 C4 5.5 5 6.5 6.5 7 L8 6 L10 8 L8.5 10 C4 9.5 0.5 6 0 1.5 Z"/></svg>555-214-870</li>
      <li><svg viewBox="0 0 10 10"><rect x="2.5" y="0" width="5" height="10" rx="1"/></svg>555-309-412</li>
      <li><svg viewBox="0 0 10 10"><rect x="0" y="2" width="10" height="6" rx="0.5"/></svg>greg@haldenfinance.com</li>
      <li><svg viewBox="0 0 10 10"><circle cx="5" cy="5" r="5"/></svg>www.haldenfinance.com</li>
    </ul>
    <p class="address">Street Name, City<br>State, zip code</p>
  </section>

  <section class="card card--back">
    <p class="back-brand">HALDEN FINANCE</p>
    <p class="back-web">www.haldenfinance.com</p>
  </section>
</body>
</html>
```